Rocket business card

Modern business card design, use of color is good with clean space too.

Things to include on card:

Quote: I add fuel to your optometry practice

- Eyewear Sales
- Admin Duties
- Revenue Collection
- Leadership
- Tech Adoption
- COGS Reduction
- Product Sourcing
-Medical Growth

Dalton Vessey, CEO
Glint Harbor
Text Me! 847-302-1964
dalton@glintharbor.example

```html
<!DOCTYPE html>
<html lang="en">
<head>
<meta charset="utf-8">
<title>Glint Harbor – Business Card</title>
<link href="https://fonts.googleapis.com/css2?family=Roboto:wght@300;400;700&display=swap" rel="stylesheet">
<style>
  :root {
    --bg: #e9e9ea;
    --card: #ffffff;
    --ink: #111111;
    --muted: #555555;
    --orange: #f08a1c;
    --orange-deep: #e8432c;
  }
  * { box-sizing: border-box; margin: 0; padding: 0; }
  html, body { width: 1200px; height: 900px; overflow: hidden; }
  body {
    background: var(--bg);
    font-family: "Roboto", Arial, sans-serif;
    position: relative;
  }
  .card {
    position: absolute;
    left: 250px;
    width: 700px;
    height: 400px;
    background: var(--card);
    box-shadow: 0 2px 6px rgba(0,0,0,0.08);
  }
  .card--front { top: 40px; }
  .card--back { top: 460px; }

  .brand { display: flex; flex-direction: column; align-items: center; gap: 18px; }
  .brand__dot {
    border-radius: 50%;
    background: linear-gradient(135deg, var(--orange), var(--orange-deep));
  }
  .brand__name {
    color: var(--ink);
    font-weight: 400;
    letter-spacing: 0.12em;
    text-transform: uppercase;
    white-space: nowrap;
  }

  .card--front .brand {
    position: absolute; left: 0; right: 0; top: 92px;
  }
  .card--front .brand__dot { width: 130px; height: 130px; }
  .card--front .brand__name { font-size: 48px; }

  .card--back .brand {
    position: absolute; left: 70px; top: 112px; width: 250px; gap: 12px;
  }
  .card--back .brand__dot { width: 72px; height: 72px; }
  .card--back .brand__name { font-size: 27px; }

  .divider {
    position: absolute; left: 345px; top: 96px;
    width: 2px; height: 150px; background: var(--orange);
  }
  .contact { position: absolute; left: 372px; top: 92px; }
  .contact__name { color: var(--orange); font-weight: 700; font-size: 30px; }
  .contact__title { color: var(--ink); font-size: 15px; margin-top: 4px; }
  .contact__list { list-style: none; margin-top: 22px; }
  .contact__item {
    display: flex; align-items: center; gap: 10px;
    color: var(--muted); font-size: 15px; margin-bottom: 10px;
  }
  .contact__item svg { width: 18px; height: 18px; flex: none; }

  .services {
    position: absolute; left: 0; right: 0; bottom: 46px;
    text-align: center; color: var(--muted);
    font-size: 16.5px; font-weight: 400; line-height: 1.45;
  }
</style>
</head>
<body>
  <section class="card card--front">
    <div class="brand">
      <div class="brand__dot"></div>
      <div class="brand__name">Glint Harbor</div>
    </div>
  </section>

  <section class="card card--back">
    <div class="brand">
      <div class="brand__dot"></div>
      <div class="brand__name">Glint Harbor</div>
    </div>
    <div class="divider"></div>
    <div class="contact">
      <div class="contact__name">Dalton Vessey</div>
      <div class="contact__title">CEO</div>
      <ul class="contact__list">
        <li class="contact__item">
          <svg viewBox="0 0 24 24" aria-hidden="true"><path fill="#f08a1c" d="M6.6 10.8a15.1 15.1 0 0 0 6.6 6.6l2.2-2.2a1 1 0 0 1 1-.25 11.4 11.4 0 0 0 3.6.57 1 1 0 0 1 1 1V20a1 1 0 0 1-1 1A17 17 0 0 1 3 4a1 1 0 0 1 1-1h3.5a1 1 0 0 1 1 1c0 1.25.2 2.45.57 3.57a1 1 0 0 1-.25 1z"/></svg>
          847-302-1964
        </li>
        <li class="contact__item">
          <svg viewBox="0 0 24 24" aria-hidden="true"><path fill="#f08a1c" d="M2 5h20v14H2z"/><path fill="none" stroke="#fff" stroke-width="1.6" d="M2.5 5.5 12 13l9.5-7.5"/></svg>
          dalton@glintharbor.example
        </li>
      </ul>
    </div>
    <p class="services">
      Eyewear Sales - Admin Duties - Revenue Collection - Leadership<br>
      Tech Adoption - COGS Reduction - Product Sourcing - Medical Growth
    </p>
  </section>
</body>
</html>
```